Business Card for Harborline Vessel

Hello, Will you do a business card design for Harborline Vessel? I attached a card from an old business of mine that I would like to copy.

The new info is:
Dennis Hollow
Owner
251-374-2908

Adress is:
41937 Pelican Ln, Orange Beach AL 36561

Email: dennis@harborlinevesselworks.example

Website is: www.harborlinevesselworks.example

Please use the new harborline vessel logo

Requirements
Must have
• QR Code for contact information

```html
<!DOCTYPE html>
<html lang="en">
<head>
<meta charset="utf-8">
<title>Harborline Vessel – Business Card</title>
<link rel="stylesheet" href="https://fonts.googleapis.com/css2?family=Montserrat:wght@500;600;700&display=swap">
<style>
  :root {
    --stage: #8b8c90;
    --ink: #111111;
    --paper: #ebebec;
    --paper-light: #f4f4f4;
    --brand-red: #b82a1e;
    --white: #ffffff;
  }
  * { box-sizing: border-box; margin: 0; padding: 0; }
  html, body { width: 900px; height: 1200px; overflow: hidden; }
  body {
    background: var(--stage);
    font-family: "Montserrat", sans-serif;
    position: relative;
  }
  .card {
    position: absolute;
    left: 135px;
    width: 632px;
    height: 363px;
    overflow: hidden;
  }
  .card--front { top: 212px; }
  .card--back { top: 627px; }

  .card__pattern { position: absolute; inset: 0; }
  .card--front .card__pattern {
    background: radial-gradient(ellipse at 95% 15%, #4a4848 0%, #242222 40%, var(--ink) 75%);
  }
  .card--back .card__pattern {
    background: linear-gradient(135deg, var(--paper-light), var(--paper));
  }

  .brand {
    position: absolute;
    font-weight: 700;
    text-transform: uppercase;
    line-height: 1.05;
    white-space: nowrap;
  }
  .brand--front {
    left: 105px; top: 122px;
    width: 422px;
    color: var(--white);
    font-size: 58px;
  }
  .brand--back {
    left: 30px; top: 40px;
    color: var(--ink);
    font-size: 34px;
  }

  .person {
    position: absolute;
    right: 32px; top: 30px;
    text-align: right;
  }
  .person__name {
    color: var(--brand-red);
    font-weight: 600;
    font-size: 37px;
    letter-spacing: -0.5px;
    line-height: 1.1;
  }
  .person__role {
    color: var(--ink);
    font-weight: 500;
    font-size: 22px;
    margin-top: 4px;
  }

  .phone {
    position: absolute;
    left: 30px; top: 198px;
    display: flex; align-items: center; gap: 12px;
    color: var(--brand-red);
    font-weight: 700;
    font-size: 23px;
    letter-spacing: 3px;
  }
  .contact {
    position: absolute;
    left: 30px; top: 256px;
    list-style: none;
  }
  .contact__item {
    display: flex; align-items: center; gap: 10px;
    height: 25.5px;
    color: var(--ink);
    font-weight: 500;
    font-size: 17.5px;
    letter-spacing: 0.4px;
  }
  .icon { width: 18px; height: 18px; fill: var(--brand-red); flex: none; }

  .qr {
    position: absolute;
    right: 32px; bottom: 30px;
    width: 104px; height: 104px;
    background: var(--white);
    border: 6px solid var(--ink);
  }
</style>
</head>
<body>

  <section class="card card--front">
    <div class="card__pattern" role="img" aria-label="Dark charcoal background with a faint repeating hex-nut pattern"></div>
    <p class="brand brand--front">Harborline<br>Vessel</p>
  </section>

  <section class="card card--back">
    <div class="card__pattern" role="img" aria-label="Light grey background with a repeating white hex-nut pattern"></div>

    <p class="brand brand--back">Harborline<br>Vessel</p>

    <div class="person">
      <p class="person__name">Dennis Hollow</p>
      <p class="person__role">Owner</p>
    </div>

    <p class="phone">
      <svg class="icon" viewBox="0 0 24 24" aria-hidden="true"><path d="M6.6 10.8a15.1 15.1 0 0 0 6.6 6.6l2.2-2.2a1 1 0 0 1 1-.25 11.4 11.4 0 0 0 3.6.57 1 1 0 0 1 1 1V20a1 1 0 0 1-1 1A17 17 0 0 1 3 4a1 1 0 0 1 1-1h3.5a1 1 0 0 1 1 1c0 1.25.2 2.45.57 3.57a1 1 0 0 1-.25 1z"/></svg>
      251-374-2908
    </p>

    <ul class="contact">
      <li class="contact__item">
        <svg class="icon" viewBox="0 0 24 24" aria-hidden="true"><path d="M12 2a7 7 0 0 0-7 7c0 5.2 7 13 7 13s7-7.8 7-13a7 7 0 0 0-7-7zm0 9.5A2.5 2.5 0 1 1 12 6.5a2.5 2.5 0 0 1 0 5z"/></svg>
        41937 Pelican Ln, Orange Beach AL 36561
      </li>
      <li class="contact__item">
        <svg class="icon" viewBox="0 0 24 24" aria-hidden="true"><path d="M2 5h20v2l-10 7L2 7z M2 9l10 7 10-7v10H2z"/></svg>
        dennis@harborlinevesselworks.example
      </li>
      <li class="contact__item">
        <svg class="icon" viewBox="0 0 24 24" aria-hidden="true"><path d="M5 2l14 11h-6.5l3.6 7.2-2.6 1.3-3.6-7.3L5 19z"/></svg>
        www.harborlinevesselworks.example
      </li>
    </ul>

    <div class="qr" role="img" aria-label="QR code linking to Dennis Hollow's contact information"></div>
  </section>

</body>
</html>
```